Commercial Real Estate

We need a business card design for a new commercial real estate business that specializes in apartment building brokerage. Not individual units but the entire complex. We find and represent the owners existing buildings and well as new buyers for those buildings. The design should convey trust, integrity, knowledge and growth. It should be easily read.

Target Market(s)

40 to 65 years old

Industry/Entity Type

Real Estate

```html
<!DOCTYPE html>
<html lang="en">
<head>
<meta charset="utf-8">
<title>Stonegate Business Card</title>
<link rel="stylesheet" href="https://fonts.googleapis.com/css2?family=Tinos:wght@700&family=PT+Sans:wght@400&display=swap">
<style>
  :root {
    --page-bg: #e7e9ea;
    --card-white: #ffffff;
    --teal: #14b0aa;
    --teal-light: #5cc8c3;
    --teal-text: #3fb6b0;
    --swoosh-grey: #b9bdbf;
    --mark-grey: #4f5d5c;
    --icon-grey: #5a6463;
  }
  * { margin: 0; padding: 0; box-sizing: border-box; }
  html, body {
    width: 1200px; height: 1000px; overflow: hidden;
    background: var(--page-bg);
  }
  .business-card {
    position: absolute; left: 100px; top: 214px;
    width: 1000px; height: 571px;
    background: var(--card-white);
    overflow: hidden;
    box-shadow: 0 6px 18px rgba(0,0,0,0.18);
  }
  .card-waves { position: absolute; inset: 0; }
  .company-heading {
    position: absolute; left: 70px; top: 92px;
    font-family: "Tinos", "Times New Roman", serif;
    font-weight: 700; font-size: 46px; letter-spacing: 1px;
    color: var(--teal-text);
  }
  .contact-list {
    position: absolute; left: 72px; top: 236px;
    list-style: none;
    font-family: "PT Sans", Arial, sans-serif;
    font-size: 24px; color: var(--teal-text);
  }
  .contact-list li {
    display: flex; align-items: center; gap: 12px;
    height: 36px;
  }
  .contact-icon { width: 22px; height: 22px; flex: none; }
  .brand-name {
    position: absolute; left: 640px; top: 120px; width: 300px;
    text-align: center;
    font-family: "Tinos", "Times New Roman", serif;
    font-weight: 700; color: var(--mark-grey);
  }
  .brand-name .brand-square {
    display: block; width: 26px; height: 26px; margin: 0 auto 18px;
    background: var(--teal);
  }
  .brand-name .brand-word { font-size: 48px; letter-spacing: 1px; display: block; }
  .brand-name .brand-tagline { font-size: 18px; letter-spacing: 2px; display: block; margin-top: 4px; }
</style>
</head>
<body>
  <div class="business-card">
    <svg class="card-waves" viewBox="0 0 1000 571" width="1000" height="571">
      <defs>
        <linearGradient id="band-gradient" x1="0" y1="0" x2="1" y2="0">
          <stop offset="0" stop-color="var(--teal)"/>
          <stop offset="0.55" stop-color="var(--teal-light)"/>
          <stop offset="1" stop-color="var(--teal)"/>
        </linearGradient>
      </defs>
      <path class="corner-band" d="M560 0 L1000 0 L1000 125 C 950 45, 800 6, 560 0 Z" fill="var(--teal)"/>
      <path class="corner-swoosh" d="M560 0 C 800 6, 950 45, 1000 125 L1000 140 C 945 60, 800 16, 560 0 Z" fill="var(--swoosh-grey)"/>
      <path class="bottom-swoosh" d="M0 470 C 250 400, 550 430, 780 405 C 920 385, 990 270, 1000 175 L1000 195 C 990 290, 920 405, 780 425 C 550 450, 250 420, 0 490 Z" fill="var(--swoosh-grey)"/>
      <path class="bottom-band" d="M0 490 C 250 420, 550 450, 780 425 C 920 405, 990 290, 1000 195 L1000 571 L0 571 Z" fill="url(#band-gradient)"/>
    </svg>

    <h1 class="company-heading">STONEGATE</h1>

    <ul class="contact-list">
      <li>
        <svg class="contact-icon" viewBox="0 0 24 24"><path d="M3 12 L12 4 L21 12 M6 10 V20 H18 V10 M10 20 V14 H14 V20" fill="none" stroke="var(--icon-grey)" stroke-width="2"/></svg>
        Stonegate Buildings
      </li>
      <li>
        <svg class="contact-icon" viewBox="0 0 24 24"><rect x="7" y="3" width="10" height="18" rx="2" fill="none" stroke="var(--icon-grey)" stroke-width="2"/><rect x="9" y="6" width="6" height="7" fill="var(--icon-grey)"/></svg>
        0000030,004700
      </li>
      <li>
        <svg class="contact-icon" viewBox="0 0 24 24"><circle cx="12" cy="12" r="9" fill="none" stroke="var(--icon-grey)" stroke-width="2"/><path d="M3 12 H21 M12 3 C 7 8, 7 16, 12 21 M12 3 C 17 8, 17 16, 12 21" fill="none" stroke="var(--icon-grey)" stroke-width="1.6"/></svg>
        www.stonegate-homes.com
      </li>
      <li>
        <svg class="contact-icon" viewBox="0 0 24 24"><rect x="3" y="6" width="18" height="12" fill="none" stroke="var(--icon-grey)" stroke-width="2"/><path d="M3 6 L12 13 L21 6" fill="none" stroke="var(--icon-grey)" stroke-width="2"/></svg>
        hello@stonegatemail.com
      </li>
    </ul>

    <div class="brand-name">
      <span class="brand-square"></span>
      <span class="brand-word">STONEGATE</span>
      <span class="brand-tagline">Property Investments</span>
    </div>
  </div>
</body>
</html>
```